Plumbing Company After Business Card

Business card for a plumbing business that offers a variety of plumbing services including maintenance, domestic and commercial plumbing. My main focus is to offer high quality professional service. A logo on the card would be ideal. Any other questions feel free to email. Cheers

Looking for something modern and upmarket with preferably a matte black background

Business name is Keystone Plumbing and Gas

Industry/Entity Type

Plumbing

Contact Information for Business Card

Keystone Plumbing and Gas
Marcus Thornell
0427915368
14 Corrigan Road, Elmvale 3561
keystoneplumbing@mailbay.com.au
ABN 52 647 183 925

Font styles to use
Sans Serif

Colors
1b1b1b
ffffff
3377b5

Requirements
Must have
• Domestic
• Commercial
• Maintenance

```html
<!DOCTYPE html>
<html lang="en">
<head>
<meta charset="utf-8">
<title>Keystone Plumbing and Gas – Business Card</title>
<link rel="stylesheet" href="https://fonts.googleapis.com/css2?family=Ubuntu:wght@400;700&display=swap">
<style>
  :root {
    --canvas: #ffffff;
    --frame: #cfcfcf;
    --card-black: #000000;
    --brand-blue: #0f6fa1;
    --brand-blue-soft: #0c5a84;
    --ink-dark: #1b1b1b;
    --accent-gold: #f2b705;
  }
  html, body {
    margin: 0;
    padding: 0;
    width: 1200px;
    height: 973px;
    overflow: hidden;
    background: var(--canvas);
  }
  .sheet {
    position: relative;
    width: 1198px;
    height: 971px;
    border: 1px solid var(--frame);
  }
  .card {
    position: absolute;
    width: 902px;
    height: 427px;
    background: var(--card-black);
    overflow: hidden;
  }
  .card--front { left: 46px; top: 43px; }
  .card--back { left: 249px; top: 502px; width: 904px; height: 426px; }

  .front-panel {
    position: absolute;
    inset: 0;
  }
  .wordmark {
    font-family: "Ubuntu", sans-serif;
    font-weight: 700;
    color: var(--brand-blue);
    letter-spacing: 1px;
    white-space: nowrap;
    margin: 0;
  }
  .card--front .wordmark {
    position: absolute;
    left: 60px;
    top: 158px;
    font-size: 68px;
    line-height: 1;
  }
  .contact {
    position: absolute;
    right: 52px;
    top: 130px;
    margin: 0;
    text-align: right;
    font-family: "Ubuntu", sans-serif;
    font-weight: 700;
    font-size: 21px;
    line-height: 35px;
    color: var(--ink-dark);
    white-space: nowrap;
  }
  .contact span { display: block; }

  .card--back .wordmark {
    position: absolute;
    left: 0;
    right: 0;
    top: 84px;
    text-align: center;
    font-size: 62px;
    line-height: 1;
  }
  .tagline {
    position: absolute;
    left: 0;
    right: 0;
    top: 170px;
    text-align: center;
    margin: 0;
    font-family: "Ubuntu", sans-serif;
    font-size: 19px;
    color: var(--accent-gold);
  }
  .services {
    position: absolute;
    left: 0;
    top: 234px;
    width: 100%;
    margin: 0;
    padding: 0;
    list-style: none;
  }
  .service {
    position: absolute;
    width: 200px;
    margin-left: -100px;
    text-align: center;
  }
  .service--maintenance { left: 236px; }
  .service--domestic { left: 458px; }
  .service--commercial { left: 676px; }
  .service-icon {
    display: block;
    width: 114px;
    height: 112px;
    margin: 0 auto;
  }
  .service-icon--placeholder {
    width: 104px;
    height: 112px;
    border-radius: 8px;
    background: linear-gradient(180deg, var(--brand-blue) 0%, var(--brand-blue-soft) 100%);
  }
  .service-label {
    display: block;
    margin-top: 10px;
    font-family: "Ubuntu", sans-serif;
    font-size: 21px;
    color: var(--brand-blue);
  }
</style>
</head>
<body>
<main class="sheet">

  <section class="card card--front" aria-label="Business card front">
    <svg class="front-panel" width="902" height="427" viewBox="0 0 902 427" aria-hidden="true">
      <polygon points="507,0 902,0 902,427 429,427" fill="var(--brand-blue)"/>
    </svg>
    <p class="wordmark">KEYSTONE</p>
    <p class="contact">
      <span>Marcus Thornell</span>
      <span>0427915368</span>
      <span>14 Corrigan Road, Elmvale 3561</span>
      <span>keystoneplumbing@mailbay.com.au</span>
      <span>ABN 52 647 183 925</span>
    </p>
  </section>

  <section class="card card--back" aria-label="Business card back">
    <p class="wordmark">KEYSTONE</p>
    <p class="tagline">Plumbing and Gas</p>
    <ul class="services">
      <li class="service service--maintenance">
        <span class="service-icon service-icon--placeholder" role="img" aria-label="Icon of a tradesman in a hard hat holding a wrench"></span>
        <span class="service-label">Maintenance</span>
      </li>
      <li class="service service--domestic">
        <svg class="service-icon" viewBox="0 0 114 112" aria-hidden="true">
          <path d="M57 4 L110 52 L100 62 L57 23 L14 62 L4 52 Z" fill="var(--brand-blue)"/>
          <rect x="80" y="10" width="13" height="30" fill="var(--brand-blue)"/>
          <path d="M22 60 L57 29 L92 60 L92 110 L22 110 Z" fill="var(--brand-blue)"/>
        </svg>
        <span class="service-label">Domestic</span>
      </li>
      <li class="service service--commercial">
        <svg class="service-icon" viewBox="0 0 114 112" aria-hidden="true">
          <rect x="12" y="4" width="90" height="10" rx="3" fill="var(--brand-blue)"/>
          <path d="M8 18 H106 L110 40 Q101 50 92 40 Q83 50 74 40 Q65 50 57 40 Q49 50 40 40 Q31 50 22 40 Q13 50 4 40 Z" fill="var(--brand-blue)"/>
          <rect x="14" y="50" width="86" height="52" fill="none" stroke="var(--brand-blue)" stroke-width="7"/>
          <line x1="40" y1="52" x2="40" y2="102" stroke="var(--brand-blue)" stroke-width="6"/>
          <line x1="48" y1="70" x2="60" y2="58" stroke="var(--brand-blue)" stroke-width="5"/>
          <rect x="4" y="102" width="106" height="8" rx="3" fill="var(--brand-blue)"/>
        </svg>
        <span class="service-label">Commercial</span>
      </li>
    </ul>
  </section>

</main>
</body>
</html>
```